RKS Rovalin Kestra Sulvane company brochure

We need the design of brochure of a company that provides consultancy, design and supply of key equipment in the field of Wastewater, clean water, organic waste anaerobic treatment and green energy production for Industries. The attached files are:
RKS wording in english that describes activities
Some drawings (useful for design)
Presentation (in italian)
It would be nice to have a 4 pages brochure possibly in double language (english and italian).

Target Market(s)

water and waste

Industry/Entity Type

It Company

Colors

Designer to choose colors to be used in the design.

Requirements
Must have
• use the logo RKS as per attached docs

```html
<!DOCTYPE html>
<html lang="en">
<head>
<meta charset="utf-8">
<title>RKS Rovalin Kestra Sulvane – Brochure Cover</title>
<link href="https://fonts.googleapis.com/css2?family=Lato:ital,wght@0,400;0,700;1,400&family=Open+Sans:wght@600;700&display=swap" rel="stylesheet">
<style>
  :root {
    --backdrop: #4a4a4a;
    --paper: #ffffff;
    --mist-light: #f4f4f4;
    --mist-mid: #e6e6e6;
    --mist-dark: #d6d6d6;
    --brand-blue: #1a73b5;
    --brand-blue-light: #3a88c0;
    --brand-blue-deep: #10629f;
    --rule-blue: #1b6fb2;
    --green-top: #3d8a1e;
    --green-bottom: #6b7e2a;
    --orange-top: #c9542a;
    --orange-bottom: #ee4a10;
    --accent-red: #e5400e;
    --ink: #1d1d1d;
    --heading-blue: #0e4f8a;
    --link-blue: #2a73b8;
  }
  * { box-sizing: border-box; margin: 0; padding: 0; }
  html, body { width: 1200px; height: 1200px; overflow: hidden; }
  body { background: var(--backdrop); font-family: "Lato", sans-serif; }

  .spread {
    position: absolute; left: 40px; top: 204px;
    width: 1120px; height: 792px;
    background: var(--paper);
    overflow: hidden;
  }
  .block { position: absolute; }

  /* back cover */
  .back-mist { left: 0; top: 0; width: 561px; height: 207px;
    background: linear-gradient(180deg, var(--mist-light) 0%, var(--mist-mid) 55%, var(--mist-dark) 100%); }
  .back-band { left: 0; top: 207px; width: 561px; height: 393px;
    background: linear-gradient(155deg, var(--brand-blue) 0%, var(--brand-blue-light) 30%, var(--brand-blue) 50%, #2f7fb8 70%, var(--brand-blue-deep) 100%); }
  .back-photo { left: 48px; top: 148px; width: 293px; height: 213px;
    border: 3px solid var(--paper);
    box-shadow: 0 1px 4px rgba(0,0,0,0.25);
    background: linear-gradient(180deg,
      #b4c0cc 0%, #a7b0b8 18%, #7e7466 32%, #8f8f86 42%,
      #a89a6a 50%, #8c8270 58%, #5f6d33 70%, #6b7a3a 76%,
      #b29d7c 84%, #c7b397 100%); }

  .back-brand { left: 38px; top: 702px; width: 220px;
    display: flex; align-items: center; gap: 8px; }
  .brand-mark { width: 14px; height: 14px; background: var(--rule-blue); flex: none; }
  .brand-name { font-family: "Open Sans", sans-serif; font-weight: 700;
    color: var(--heading-blue); font-size: 13.5px; line-height: 1.2; white-space: nowrap; }

  .contact { left: 264px; top: 642px; width: 290px; }
  .contact h2 { font-family: "Lato", sans-serif; font-weight: 400;
    font-size: 20px; color: var(--heading-blue); margin-bottom: 12px; letter-spacing: -0.2px; }
  .contact p { font-size: 12.5px; color: var(--ink); line-height: 24px; }
  .contact b { font-weight: 700; }

  /* spine strips */
  .strip-green { left: 561px; top: 0; width: 125px; height: 207px;
    background: linear-gradient(180deg, var(--green-top), var(--green-bottom)); }
  .strip-orange { left: 561px; top: 600px; width: 125px; height: 192px;
    background: linear-gradient(180deg, var(--orange-top), var(--orange-bottom)); }
  .spine-rule { left: 689px; top: 0; width: 5px; height: 792px; background: var(--rule-blue); }

  /* front cover */
  .front-mist { left: 694px; top: 0; width: 426px; height: 207px;
    background: linear-gradient(180deg, var(--mist-light) 0%, var(--mist-mid) 55%, var(--mist-dark) 100%); }
  .front-photo { left: 561px; top: 207px; width: 559px; height: 393px;
    background: linear-gradient(180deg,
      #e4eaf1 0%, #d3dbe3 14%, #b9c0c6 26%, #a4abb0 38%,
      #8e9599 50%, #6d7478 60%, #7f8a86 66%, #b8bdbb 74%,
      #d9dcda 84%, #c9cccb 100%); }

  .front-brand { left: 694px; top: 70px; width: 426px;
    display: flex; justify-content: center; align-items: center; gap: 10px; }
  .front-brand .brand-mark { width: 22px; height: 22px; }
  .front-brand .brand-name { font-size: 24px; }

  .mission { left: 694px; top: 640px; width: 426px; text-align: center; }
  .mission h1 { font-family: "Open Sans", sans-serif; font-weight: 600;
    font-size: 22px; color: var(--accent-red); margin-bottom: 4px; }
  .mission .lead { font-family: "Open Sans", sans-serif; font-weight: 700;
    font-size: 14px; color: var(--ink); line-height: 20px; }
  .mission .value { margin-top: 14px; font-size: 15px; line-height: 21px; color: var(--link-blue); }
  .mission .value strong { display: block; color: var(--accent-red); font-weight: 700; }
</style>
</head>
<body>
  <main class="spread">
    <div class="block back-mist" role="img" aria-label="Water droplets on a light grey surface"></div>
    <div class="block back-band" role="img" aria-label="Blue-tinted faded aerial view of a treatment plant with basins and buildings"></div>
    <div class="block back-photo" role="img" aria-label="Photo of an outdoor circular clarifier basin with yellow walkway, trees behind"></div>

    <div class="block back-brand">
      <span class="brand-mark"></span>
      <span class="brand-name">RKS Rovalin Kestra Sulvane</span>
    </div>

    <section class="block contact">
      <h2>CONTACT US</h2>
      <p>RKS Srl – Via dei Mulini 27/4 – Novara</p>
      <p><b>Telefono:</b> 011.5550192</p>
      <p><b>Cellulare:</b> 335 555 0148</p>
      <p><b>PIVA:</b> 12345670018</p>
    </section>

    <div class="block strip-green"></div>
    <div class="block strip-orange"></div>
    <div class="block spine-rule"></div>

    <div class="block front-mist" role="img" aria-label="Water droplets on a light grey surface"></div>
    <div class="block front-brand">
      <span class="brand-mark"></span>
      <span class="brand-name">RKS Rovalin Kestra Sulvane</span>
    </div>
    <div class="block front-photo" role="img" aria-label="Photo of a steel flotation tank with stairs, walkways and green pumps on a rooftop"></div>

    <section class="block mission">
      <h1>RKS ltd (RKS) has the mission</h1>
      <p class="lead">to solve any client’s environmental problem<br>with best process solution available on the market</p>
      <p class="value">most reliable and economical both<strong>on the CAPEX and OPEX</strong></p>
    </section>
  </main>
</body>
</html>
```